Brightway Inc. Business Card Design

Brightway Inc. is in search of a great clean design for our business cards!

Looking to incorporate our full logo and watermark on side one (however, I am open to having the text and watermark separated within the design.)

On side two, I am looking to have contact information (Name, Position, Phone #, Email, Website (www.thebrightway.ca). Can have the logo and/or watermark as part of the design if applicable.

Please add tagline "Where Shine Counts" on either side 1 or 2. This tagline can be in a sans serif, serif or cursive font as long as it compliments overall design. Capitalization can be title or sentence case depending on how it fits within the design.

Get creative!! Looking for a clean, crisp, premium design! Looking for a glossy card finish with spot UV features when printed. Cards will also be printed with rounded corners. Standard dimensions (3.5 x 2).

Target Market(s)

B2B - primary clients are business owners or property management corporations. (residential jobs are few and far between)

Industry/Entity Type

Business

Contact Information for Business Card

- clean, crisp design
- double sided
- spot UV accents and glossy finish upon printing
- standard business card size (3.5 x 2) with rounded corners
- please see project description for requirements per side

Font styles to use
Sans Serif

Requirements
Must have
• - adequate bleeds with print ready files
• - cohesive design elements between side 1 & 2
• - spot UV elements (can be on both sides or just one, use your discretion)
• - colour pallet should match the logo file provided
• - incorporate tagline "where shine counts" (this tagline can be in a serif or sans serif font as long as it is complimentary to the overall design.
Nice to have
• - Premium elements with a clean design
Should not have
• - Please omit cartoon or whimsical like designs, think premium.
• - Colours should not stray from the pallet of the provided logo.

```html
<!DOCTYPE html>
<html lang="en">
<head>
<meta charset="utf-8">
<title>Brightway Inc. Business Card</title>
<link rel="stylesheet" href="https://fonts.googleapis.com/css2?family=Roboto:wght@400;500;700&family=Montserrat:wght@400&display=swap">
<style>
  :root {
    --teal: #0f9a98;
    --navy: #1c1d45;
    --grey: #9b9b9b;
    --card-top: #efefef;
    --card-bottom: #e2e2e2;
    --backdrop: #dadada;
    --ink: #22223a;
  }
  * { box-sizing: border-box; margin: 0; padding: 0; }
  html, body { width: 1200px; height: 576px; overflow: hidden; }
  body {
    background: var(--backdrop);
    font-family: "Roboto", sans-serif;
    color: var(--ink);
    position: relative;
  }
  .card {
    position: absolute;
    top: 138px;
    width: 484px;
    height: 293px;
    border-radius: 14px;
    background: linear-gradient(160deg, var(--card-top), var(--card-bottom));
    overflow: hidden;
  }
  .card--front { left: 82px; }
  .card--back { left: 602px; }

  .wordmark {
    display: flex;
    align-items: center;
    gap: 10px;
    color: var(--teal);
    font-weight: 700;
    letter-spacing: 0.5px;
    white-space: nowrap;
  }
  .wordmark__square {
    display: inline-block;
    background: var(--navy);
  }
  .card--front .wordmark {
    position: absolute;
    left: 0; right: 0; top: 118px;
    justify-content: center;
    font-size: 44px;
  }
  .card--front .wordmark__square { width: 38px; height: 38px; }
  .card--back .wordmark {
    position: absolute;
    left: 26px; top: 30px;
    font-size: 42px;
  }
  .card--back .wordmark__square { width: 36px; height: 36px; }

  .contact-name {
    position: absolute;
    left: 26px; top: 116px;
    display: flex;
    align-items: center;
  }
  .contact-name__person {
    color: var(--teal);
    font-weight: 700;
    font-size: 21px;
    padding-right: 7px;
    border-right: 1px solid var(--ink);
    line-height: 26px;
  }
  .contact-name__role { font-size: 13px; padding-left: 7px; }

  .contact-address {
    position: absolute;
    left: 26px; top: 160px;
    font-size: 13px;
  }
  .contact-list {
    position: absolute;
    left: 30px; top: 182px;
    list-style: none;
    font-size: 13px;
  }
  .contact-list li {
    display: flex;
    align-items: center;
    gap: 8px;
    height: 19px;
  }
  .contact-list svg { width: 11px; height: 11px; fill: var(--teal); flex: none; }
  .contact-list .accent { color: var(--teal); }

  .wave { position: absolute; left: 0; top: 0; width: 484px; height: 293px; }

  .tagline {
    position: absolute;
    right: 24px; top: 228px;
    text-align: right;
    font-family: "Montserrat", sans-serif;
    font-size: 13px;
    letter-spacing: 1.6px;
    line-height: 23px;
    color: #ffffff;
    text-transform: uppercase;
  }
</style>
</head>
<body>

  <section class="card card--front" aria-label="Card front">
    <div class="wordmark"><span class="wordmark__square"></span>BRIGHTWAY INC.</div>
  </section>

  <section class="card card--back" aria-label="Card back">
    <svg class="wave" viewBox="0 0 484 293" aria-hidden="true">
      <path d="M0,238 C60,258 150,274 260,262 C180,272 80,268 0,256 Z" fill="var(--grey)"/>
      <path d="M0,293 L0,270 C120,300 250,252 330,226 C400,206 440,206 484,206 L484,293 Z" fill="var(--teal)"/>
      <path d="M40,252 C150,285 260,232 340,207 C400,190 450,191 484,191" fill="none" stroke="var(--navy)" stroke-width="5"/>
    </svg>

    <div class="wordmark"><span class="wordmark__square"></span>BRIGHTWAY INC.</div>

    <div class="contact-name">
      <span class="contact-name__person">Maya Lindqvist</span>
      <span class="contact-name__role">Managing Director</span>
    </div>

    <p class="contact-address">48 Harbour Lane, Suite 2, Halton 417</p>

    <ul class="contact-list">
      <li>
        <svg viewBox="0 0 12 12"><path d="M1,3 C1,1.5 2,1 6,1 C10,1 11,1.5 11,3 L9,4 L8,3 L4,3 L3,4 Z M3,5 L9,5 L11,10 L1,10 Z"/></svg>
        1800-555-0147
      </li>
      <li>
        <svg viewBox="0 0 12 12"><path d="M0,2 H12 V10 H0 Z M1,3 L6,7 L11,3" stroke="#fff" stroke-width="0.8"/></svg>
        maya@thebrightway.ca
      </li>
      <li>
        <svg viewBox="0 0 12 12"><circle cx="6" cy="6" r="5.5"/><path d="M0.5,6 H11.5 M6,0.5 V11.5 M6,0.5 C3,3 3,9 6,11.5 M6,0.5 C9,3 9,9 6,11.5" stroke="#fff" stroke-width="0.7" fill="none"/></svg>
        <span>www.<span class="accent">thebrightway</span>.ca</span>
      </li>
    </ul>

    <p class="tagline">Where<br>Shine Counts</p>
  </section>

</body>
</html>
```